Sales sheet for printing and embroidery apparel items - Copper Fern Prints

I would like a one page flyer or sales sheet that I would use as a template to send different images of apparel we produce. I have attached examples of layouts I like.
- Ideally, it would have space for 3-5 items.
- I would like it one page only - not a folding flyer.
- Our companies name is Copper Fern Prints.
- This will be used for many different products and markets so I don't need wording/copy. You can use wording from the 7Q7 or K81 flyer.

Colors
0054AA
0677BA
7BADD7
CADEEF
E8F1F8
00AB8E
00BBA5
67D7C9
C6EFE9
E9F9F6
FFC000
F8CF3A
FAE287
FDF2CF
FEFAEE

Requirements
Must have
• Places for between 3 and 5 images of apparel (t-shirts, hats etc)

```html
<!DOCTYPE html>
<html lang="en">
<head>
<meta charset="utf-8">
<title>Copper Fern Prints – Sales Sheet</title>
<link rel="stylesheet" href="https://fonts.googleapis.com/css2?family=Oswald:wght@500;600;700&family=Poppins:wght@400;500;600&display=swap">
<style>
  :root{
    --backdrop:#b8b8b8;
    --paper:#ffffff;
    --navy:#033a60;
    --coral:#ef6160;
    --orange:#e36a46;
    --sky:#e2f1fb;
    --white:#ffffff;
    --ink:#111111;
  }
  *{box-sizing:border-box;margin:0;padding:0}
  html,body{width:955px;height:1200px;overflow:hidden}
  body{background:var(--backdrop);position:relative;font-family:"Poppins",sans-serif}
  .sheet{position:absolute;left:162px;top:127px;width:631px;height:947px;background:var(--paper);overflow:hidden}
  .abs{position:absolute}

  /* brand */
  .brand{left:22px;top:18px;width:138px;height:120px;text-align:center}
  .brand-square{width:66px;height:66px;background:var(--coral);margin:0 auto 6px}
  .brand-name{font-family:"Oswald",sans-serif;font-weight:700;color:var(--navy);font-size:21px;line-height:21px;letter-spacing:.5px;text-transform:uppercase}

  /* headline */
  .headline{left:195px;top:18px;width:410px;font-family:"Oswald",sans-serif;font-weight:600;font-size:42px;line-height:45px;letter-spacing:-1.4px;text-transform:uppercase;white-space:nowrap}
  .headline .line-top{color:var(--coral)}
  .headline .line-bottom{color:var(--navy)}

  /* navy band */
  .band{left:0;top:147px;width:631px;height:332px;background:var(--navy)}
  .accent-block{left:25px;top:455px;width:85px;height:36px;background:linear-gradient(180deg,var(--coral),var(--orange))}

  .feature{width:150px;text-align:center;color:var(--white)}
  .feature svg{display:block;margin:0 auto;stroke:var(--white);fill:none;stroke-width:1.4;stroke-linecap:round;stroke-linejoin:round}
  .feature-title{font-family:"Oswald",sans-serif;font-weight:600;font-size:20px;line-height:22px;color:var(--coral);text-transform:uppercase;letter-spacing:-.3px;margin-top:10px}
  .feature-text{font-size:12px;line-height:15px;font-weight:500;margin-top:2px}

  /* offer panel */
  .offer-frame{left:376px;top:236px;width:232px;height:331px;border:1.5px solid var(--coral)}
  .offer-panel{left:388px;top:122px;width:209px;height:432px;background:linear-gradient(180deg,var(--coral) 0%,var(--orange) 100%);text-align:center;color:var(--white)}
  .offer-title{position:absolute;left:0;right:0;top:16px;font-family:"Oswald",sans-serif;font-weight:700;font-size:38px;line-height:44px;letter-spacing:-1px;text-shadow:1px 2px 2px rgba(0,0,0,.35)}
  .offer-icon{position:absolute;left:76px;width:56px;height:56px;border-radius:50%;background:var(--white);display:flex;align-items:center;justify-content:center}
  .offer-icon::after{content:"";position:absolute;inset:4px;border-radius:50%;border:1.3px dotted var(--coral)}
  .offer-icon svg{fill:var(--navy)}
  .offer-label{position:absolute;left:0;right:0;font-size:12.5px;line-height:16px;font-weight:500}

  /* products */
  .section-title{font-family:"Oswald",sans-serif;font-weight:700;font-size:40px;line-height:44px;letter-spacing:-1.2px;text-transform:uppercase;color:var(--navy);white-space:nowrap}
  .section-title .hl{color:var(--coral)}
  .products-title{left:23px;top:516px}
  .product-slot{top:578px;width:110px;height:98px;background:var(--sky)}

  .order-title{left:24px;top:693px;font-size:37px;line-height:42px}

  /* steps */
  .step-badge{width:49px;height:49px;border-radius:50%;border:1px solid var(--coral);display:flex;align-items:center;justify-content:center}
  .step-badge span{width:42px;height:42px;border-radius:50%;background:var(--navy);display:flex;align-items:center;justify-content:center}
  .step-badge svg{stroke:var(--white);fill:none;stroke-width:1.5;stroke-linecap:round;stroke-linejoin:round}
  .step-title{font-family:"Oswald",sans-serif;font-weight:600;font-size:16px;line-height:22px;color:var(--coral);text-transform:uppercase;letter-spacing:-.6px;white-space:nowrap}
  .step-text{font-size:9.4px;line-height:11px;font-weight:500;color:var(--ink);text-align:justify;margin-top:3px}

  /* footer */
  .footer{left:0;top:844px;width:631px;height:103px;background:var(--navy)}
  .footer-call{left:22px;top:851px;font-family:"Oswald",sans-serif;font-weight:500;font-size:26px;line-height:30px;color:var(--coral);letter-spacing:-.6px;white-space:nowrap}
  .contact-line{left:24px;display:flex;align-items:center;color:var(--white);white-space:nowrap}
  .contact-line svg{margin-right:8px}
  .contact-phone{top:880px;font-family:"Oswald",sans-serif;font-weight:600;font-size:26px;line-height:32px}
  .contact-email{top:909px;font-size:16.5px;font-weight:500;line-height:24px}
  .social-dot{top:852px;width:21px;height:21px;border-radius:50%;background:var(--coral)}
  .badge-strip{left:282px;top:882px;width:327px;height:48px;background:var(--white);border-radius:12px}
  .badge{position:absolute}
</style>
</head>
<body>
<main class="sheet">

  <div class="abs brand">
    <div class="brand-square"></div>
    <div class="brand-name">Copper Fern<br>Prints</div>
  </div>

  <h1 class="abs headline">
    <div class="line-top">Order shirts for your</div>
    <div class="line-bottom">All of your retreats</div>
  </h1>

  <div class="abs band"></div>
  <div class="abs accent-block"></div>

  <!-- features -->
  <div class="abs feature" style="left:32px;top:166px">
    <svg width="60" height="62" viewBox="0 0 60 62">
      <path d="M8 30 L30 6 L52 22 L30 48 Z"/>
      <path d="M8 34 L30 52 L52 26"/>
      <path d="M8 38 L30 56 L52 30"/>
      <path d="M8 42 L30 60 L52 34"/>
      <path d="M8 30 L8 42 M52 22 L52 34"/>
      <path d="M24 12 Q32 20 40 16"/>
    </svg>
    <div class="feature-title">Low Minimums</div>
    <div class="feature-text">Order as few as 24<br>pieces to get started.</div>
  </div>

  <div class="abs feature" style="left:198px;top:166px">
    <svg width="66" height="62" viewBox="0 0 66 62">
      <path d="M8 4 L14 6 L30 52"/>
      <circle cx="32" cy="56" r="4"/>
      <path d="M36 54 L62 44"/>
      <path d="M28 26 L48 18 L56 38 L36 46 Z"/>
      <path d="M38 22 L42 32 M44 20 L48 30"/>
      <path d="M22 10 L38 4 L44 18"/>
      <path d="M2 36 H18 M6 42 H20 M2 48 H22"/>
    </svg>
    <div class="feature-title">Fast Turnaround</div>
    <div class="feature-text">2-week standard<br>delivery.</div>
  </div>

  <div class="abs feature" style="left:26px;top:305px">
    <svg width="62" height="50" viewBox="0 0 62 50">
      <circle cx="31" cy="7" r="5.5"/>
      <circle cx="18" cy="10" r="4.5"/>
      <circle cx="44" cy="10" r="4.5"/>
      <circle cx="7" cy="13" r="3.5"/>
      <circle cx="55" cy="13" r="3.5"/>
      <path d="M22 48 V26 Q22 16 31 16 Q40 16 40 26 V48 H35 V34 M27 34 V48 H22"/>
      <path d="M16 44 H11 V26 Q11 19 18 19"/>
      <path d="M46 44 H51 V26 Q51 19 44 19"/>
      <path d="M5 40 H2 V28 Q2 22 7 22 M57 40 H60 V28 Q60 22 55 22"/>
    </svg>
    <div class="feature-title">Real People</div>
    <div class="feature-text">Work with our team<br>of experts and artists.</div>
  </div>

  <div class="abs feature" style="left:198px;top:305px">
    <svg width="66" height="52" viewBox="0 0 66 52">
      <path d="M30 2 L44 8 V22 Q44 32 30 38 Q16 32 16 22 V8 Z"/>
      <circle cx="30" cy="19" r="8"/>
      <path d="M26 19 L29 22 L34 16"/>
      <path d="M6 8 L10 11 M4 20 H9 M6 32 L10 29 M54 8 L50 11 M56 20 H51 M54 32 L50 29"/>
      <path d="M4 40 Q16 36 26 42 H38 Q40 46 34 46 H24 M38 42 L56 38 Q62 38 58 44 L44 50 H20 L4 46"/>
    </svg>
    <div class="feature-title">Guaranteed</div>
    <div class="feature-text">We promise accurate,<br>quality work.</div>
  </div>

  <!-- offer panel -->
  <div class="abs offer-frame"></div>
  <aside class="abs offer-panel">
    <h2 class="offer-title">WE OFFER</h2>

    <div class="offer-icon" style="top:62px">
      <svg width="32" height="30" viewBox="0 0 32 30">
        <path d="M14 2 C5 2 0 9 1 16 C2 24 9 28 15 27 C19 26 17 22 19 20 C21 18 25 20 27 17 C30 12 24 2 14 2 Z M8 8 a3 3 0 1 0 .1 0 Z M6 16 a3 3 0 1 0 .1 0 Z M13 20 a3 3 0 1 0 .1 0 Z M16 6 a3 3 0 1 0 .1 0 Z" fill-rule="evenodd"/>
        <path d="M30 1 L32 3 L22 20 L19 18 Z"/>
      </svg>
    </div>
    <div class="offer-label" style="top:122px">Art Design</div>

    <div class="offer-icon" style="top:143px">
      <svg width="38" height="24" viewBox="0 0 38 24">
        <path d="M8 2 H26 V18 H8 Z M26 7 H32 L37 12 V18 H26 Z"/>
        <circle cx="13" cy="19" r="3.5" fill="#fff" stroke="#033a60" stroke-width="2"/>
        <circle cx="31" cy="19" r="3.5" fill="#fff" stroke="#033a60" stroke-width="2"/>
        <path d="M0 5 H6 M1 9 H6 M2 13 H6"/>
        <text x="9.5" y="12" font-family="Poppins,sans-serif" font-size="6.5" font-weight="600" font-style="italic" fill="#fff">FREE</text>
      </svg>
    </div>
    <div class="offer-label" style="top:204px">Free Shipping</div>

    <div class="offer-icon" style="top:226px">
      <svg width="30" height="30" viewBox="0 0 30 30">
        <circle cx="16" cy="8" r="7"/>
        <text x="12.7" y="11.5" font-family="Poppins,sans-serif" font-size="10" font-weight="600" fill="#fff">$</text>
        <path d="M2 20 L8 16 H16 Q19 16 18 19 H12 M18 19 L26 15 Q29 15 28 18 L18 26 H8 L4 29 L0 24 Z"/>
      </svg>
    </div>
    <div class="offer-label" style="top:287px">We Pay ALL Royalties<br>to the Movement</div>

    <div class="offer-icon" style="top:323px">
      <svg width="30" height="28" viewBox="0 0 30 28">
        <path d="M10 1 Q15 5 20 1 L29 6 L25 13 L22 11 V27 H8 V11 L5 13 L1 6 Z"/>
      </svg>
    </div>
    <div class="offer-label" style="top:384px">Many Options of Shirt<br>Styles and Colors</div>
  </aside>

  <!-- products -->
  <h2 class="abs section-title products-title">Our <span class="hl">Products</span></h2>
  <div class="abs product-slot" style="left:26px" aria-label="Apparel item 1"></div>
  <div class="abs product-slot" style="left:143px" aria-label="Apparel item 2"></div>
  <div class="abs product-slot" style="left:261px" aria-label="Apparel item 3"></div>
  <div class="abs product-slot" style="left:378px" aria-label="Apparel item 4"></div>
  <div class="abs product-slot" style="left:495px" aria-label="Apparel item 5"></div>

  <!-- how to order -->
  <h2 class="abs section-title order-title">How to <span class="hl">Start an Order</span></h2>

  <div class="abs step-badge" style="left:20px;top:751px"><span>
    <svg width="24" height="24" viewBox="0 0 24 24"><circle cx="14" cy="10" r="7"/><path d="M9 15 L3 21"/><path d="M10 12 L12 8 H16 L18 12 Z"/></svg>
  </span></div>
  <div class="abs" style="left:79px;top:744px;width:130px">
    <div class="step-title">1. Choose your ride</div>
    <p class="step-text">Send us a picture, or let us know the make and model of the vehicle you would like featured on your apparel.</p>
  </div>

  <div class="abs step-badge" style="left:225px;top:751px"><span>
    <svg width="24" height="24" viewBox="0 0 24 24"><path d="M8 2 Q12 5 16 2 L22 6 L19 10 L17 9 V21 H7 V9 L5 10 L2 6 Z"/><path d="M12 11 V17 M10 14 L12 17 L14 14"/></svg>
  </span></div>
  <div class="abs" style="left:284px;top:744px;width:120px">
    <div class="step-title">2. Pick your gear</div>
    <p class="step-text">We will help you choose your t-shirts, sweatshirts or other apparel items and determine sizes and quantities.</p>
  </div>

  <div class="abs step-badge" style="left:414px;top:751px"><span>
    <svg width="24" height="24" viewBox="0 0 24 24"><path d="M3 21 L14 10 M16 3 A5 5 0 0 0 21 10 L18 8 L16 8 L16 6 Z"/><path d="M4 4 L7 3 L10 6 L9 9 L21 21 L19 22 L7 10 L4 9 L3 6 Z"/></svg>
  </span></div>
  <div class="abs" style="left:472px;top:744px;width:138px">
    <div class="step-title">3. We customize</div>
    <p class="step-text">We make the magic happen and our team of expert artists will design your shirts and get a proof out to you. Upon order approval your order will go into production.</p>
  </div>

  <!-- footer -->
  <footer class="abs footer"></footer>
  <div class="abs footer-call">We’d love to work with you!</div>
  <div class="abs contact-line contact-phone">
    <svg width="18" height="18" viewBox="0 0 24 24"><path d="M5 2 L9 2 L11 7 L8 9 Q10 14 15 16 L17 13 L22 15 V19 Q22 22 18 22 Q3 20 2 6 Q2 2 5 2 Z" fill="none" stroke="#ef6160" stroke-width="2"/><path d="M14 3 Q20 4 21 10 M14 7 Q17 8 17 10" fill="none" stroke="#ef6160" stroke-width="2"/></svg>
    555-210-4837
  </div>
  <div class="abs contact-line contact-email">
    <svg width="16" height="12" viewBox="0 0 16 12"><rect x="0" y="0" width="16" height="12" fill="#ef6160"/><path d="M0 0 L8 7 L16 0" fill="none" stroke="#033a60" stroke-width="1.2"/></svg>
    ann@copperfern.com
  </div>

  <div class="abs social-dot" style="left:538px"></div>
  <div class="abs social-dot" style="left:563px"></div>
  <div class="abs social-dot" style="left:588px"></div>

  <div class="abs badge-strip">
    <span class="badge" style="left:19px;top:10px;width:28px;height:28px;border-radius:50%;background:#e8efe2;border:2px solid #2e6b34"></span>
    <span class="badge" style="left:58px;top:10px;width:28px;height:28px;border-radius:50%;background:#fbe3e3;border:2px solid #d8333a"></span>
    <span class="badge" style="left:97px;top:14px;width:63px;height:20px;background:#5b3f99"></span>
    <span class="badge" style="left:167px;top:14px;width:44px;height:20px;border-radius:50%;background:#2d5aa6"></span>
    <span class="badge" style="left:215px;top:10px;width:45px;height:28px;border-radius:14px;background:#3d9b35"></span>
    <span class="badge" style="left:264px;top:12px;width:44px;height:24px;border-radius:4px;background:#f2a52b"></span>
  </div>

</main>
</body>
</html>
```